I dont have a logo yet. My mind in color is navy blue and khaki maybe a tiny bit of yellow but open to ideas. name of the business is Prairie Ridge Builders. Dedicated to all sorts of construction commerical and residential. Im Tomas Verdugo owner of business<br/>Address to business is 287 N. Marbury El Paso Tx 79925 <br/>Phone is 9156820374<br/>Id like round corners i also like the see thru card a little.<br/>Open to trademark quotes

Target Market(s)

Construction

Contact Information for Business Card

PRAIRIE RIDGE BUILDERS LLC

Tomas Verdugo
Director of Operations

Commercial & Residential

9156820374
PRAIRIE.R.BUILDERS@MAILHAVEN.NET

Colors
0355a3
fff3d1

Requirements
Must have
• ROUND CORNERS
• BLUE AND KHAKI AND CLEAR
• LOGO

```html
<!DOCTYPE html>
<html lang="en">
<head>
<meta charset="UTF-8">
<title>Prairie Ridge Builders – Business Card</title>
<link rel="stylesheet" href="https://fonts.googleapis.com/css2?family=Montserrat:wght@300;400;600;700&display=swap">
<style>
  :root {
    --page-bg: #e9e6e1;
    --navy-deep: #0a1250;
    --navy: #0f1a78;
    --navy-soft: #2c3a8c;
    --bronze: #b9865a;
    --bronze-light: #c8a07a;
    --frost: #eef1f4;
    --frost-shade: #bfc5cc;
    --text-light: #e3e6f2;
    --brand-ink: #101a5c;
  }
  html, body {
    margin: 0;
    padding: 0;
    width: 1200px;
    height: 1098px;
    overflow: hidden;
    background: var(--page-bg);
    font-family: "Montserrat", sans-serif;
  }
  .card {
    position: absolute;
    left: 60px;
    top: 241px;
    width: 1080px;
    height: 615px;
    border-radius: 34px;
    overflow: hidden;
    box-shadow: 0 18px 40px rgba(0,0,0,0.22);
    background:
      radial-gradient(ellipse 520px 420px at 260px 300px, var(--navy-soft) 0%, rgba(44,58,140,0) 100%),
      linear-gradient(100deg, var(--navy-soft) 0%, var(--navy) 45%, var(--navy-deep) 100%);
  }
  .card-art {
    position: absolute;
    inset: 0;
  }
  .details {
    position: absolute;
    left: 60px;
    top: 0;
    color: var(--text-light);
    font-weight: 400;
  }
  .details p { margin: 0; position: absolute; white-space: nowrap; }
  .holder-name {
    top: 42px;
    font-size: 48px;
    font-weight: 600;
    color: var(--bronze);
  }
  .holder-role { top: 112px; font-size: 29px; }
  .services { top: 194px; font-size: 29px; line-height: 36px; }
  .address-line-1 { top: 305px; font-size: 29px; }
  .address-line-2 { top: 350px; font-size: 29px; }
  .phone, .email {
    display: flex;
    align-items: center;
    gap: 18px;
  }
  .phone { top: 400px; font-size: 30px; }
  .email { top: 452px; font-size: 27px; }
  .contact-icon { width: 24px; height: 30px; flex: none; }
  .tagline {
    top: 522px;
    font-size: 30px;
    color: var(--bronze);
    opacity: 0.85;
  }
  .brand-name {
    position: absolute;
    left: 605px;
    top: 300px;
    width: 476px;
    text-align: center;
    font-size: 31px;
    font-weight: 600;
    line-height: 35px;
    color: var(--brand-ink);
    margin: 0;
  }
  .brand-square {
    position: absolute;
    left: 813px;
    top: 150px;
    width: 60px;
    height: 60px;
    background: var(--brand-ink);
  }
</style>
</head>
<body>
  <main class="card">
    <svg class="card-art" width="1080" height="615" viewBox="0 0 1080 615" aria-hidden="true">
      <defs>
        <linearGradient id="frost-glass" x1="0" y1="0" x2="0.3" y2="1">
          <stop offset="0" stop-color="#f7f8fa"/>
          <stop offset="0.6" stop-color="var(--frost)"/>
          <stop offset="1" stop-color="var(--frost-shade)"/>
        </linearGradient>
        <linearGradient id="clear-corner" x1="0" y1="0" x2="1" y2="1">
          <stop offset="0" stop-color="#dfe3e8"/>
          <stop offset="1" stop-color="#c9ced6"/>
        </linearGradient>
      </defs>
      <!-- clear upper-right corner of the card -->
      <polygon points="740,0 1080,0 1080,400 843,391" fill="url(#clear-corner)"/>
      <!-- bronze hexagon frame -->
      <polygon points="843,-98 1125,65 1125,391 843,554 561,391 561,65" fill="var(--bronze)"/>
      <!-- clear hexagon window -->
      <polygon points="843,-47 1081,90 1081,365 843,503 605,365 605,90" fill="url(#frost-glass)"/>
    </svg>

    <section class="details">
      <p class="holder-name">Tomas Verdugo</p>
      <p class="holder-role">Director of Operations</p>
      <p class="services">Commercial &amp;<br>Residential construction</p>
      <p class="address-line-1">287 N. Marbury Dr</p>
      <p class="address-line-2">El Paso Tx 79925</p>
      <p class="phone">
        <svg class="contact-icon" viewBox="0 0 24 30" aria-hidden="true">
          <rect x="3" y="1.5" width="18" height="27" rx="3" fill="none" stroke="var(--text-light)" stroke-width="2"/>
          <line x1="9" y1="24" x2="15" y2="24" stroke="var(--text-light)" stroke-width="2"/>
        </svg>
        9156820374
      </p>
      <p class="email">
        <svg class="contact-icon" viewBox="0 0 28 20" style="width:28px;height:20px" aria-hidden="true">
          <rect x="0" y="0" width="28" height="20" fill="var(--text-light)"/>
          <polyline points="0,0 14,11 28,0" fill="none" stroke="var(--navy)" stroke-width="2"/>
          <line x1="0" y1="20" x2="10" y2="10" stroke="var(--navy)" stroke-width="2"/>
          <line x1="28" y1="20" x2="18" y2="10" stroke="var(--navy)" stroke-width="2"/>
        </svg>
        prairie.r.builders@mailhaven.net
      </p>
      <p class="tagline">Take off construction</p>
    </section>

    <div class="brand-square" aria-hidden="true"></div>
    <p class="brand-name">PRAIRIE RIDGE<br>BUILDERS LLC</p>
  </main>
</body>
</html>
```